Birchwood Forage Business Cards

I need a business card with my logo, number, Facebook account, and some information about what I am selling. Green card with logo on the front. 847-302-1596 phone number, @birchwoodforage Facebook, •Orchardgrass Hay •Alfalfa Hay •Mixed Grass Hay , and “Premium Quality Hay” all written on the back.

Target Market(s)

Hay

Contact Information for Business Card

Phone number, Facebook, different types of hay.

Colors
00AB8E
00BBA5
67D7C9
C6EFE9
E9F9F6

```html
<!DOCTYPE html>
<html lang="en">
<head>
<meta charset="utf-8">
<title>Birchwood Forage Business Cards</title>
<link href="https://fonts.googleapis.com/css2?family=Roboto:ital,wght@0,400;0,700;1,400&display=swap" rel="stylesheet">
<style>
  :root {
    --page: #dcdcdc;
    --card-white: #ffffff;
    --card-dark: #1f2021;
    --brand-green: #0fa050;
    --leaf-green: #02b66d;
    --ink: #0d0d0d;
    --light-text: #ffffff;
  }
  html, body {
    margin: 0;
    width: 1200px;
    height: 1200px;
    overflow: hidden;
    background: var(--page);
    font-family: "Roboto", Arial, sans-serif;
  }
  .canvas { position: relative; width: 1200px; height: 1200px; }
  .card {
    position: absolute;
    left: 262px;
    width: 800px;
    height: 456px;
    border-radius: 28px;
    overflow: hidden;
    transform: scale(0.8575);
    transform-origin: top left;
  }
  .card--front { top: 166px; background: var(--card-white); }
  .card--back { top: 653px; background: var(--card-dark); }

  .front-swoosh { position: absolute; inset: 0; width: 800px; height: 456px; }

  .front-contact {
    position: absolute;
    left: 65px;
    top: 328px;
    color: var(--light-text);
  }
  .front-contact__phone {
    font-weight: 700;
    font-size: 45px;
    line-height: 1;
    letter-spacing: 0.5px;
  }
  .front-contact__social {
    display: flex;
    align-items: center;
    gap: 10px;
    margin-top: 6px;
    font-style: italic;
    font-size: 29px;
  }
  .social-dot {
    width: 36px; height: 36px;
    border-radius: 50%;
    background: var(--light-text);
    flex: none;
  }

  .brand-mark {
    display: flex;
    align-items: center;
    font-weight: 700;
  }
  .brand-mark__circle { border-radius: 50%; background: var(--leaf-green); flex: none; }

  .brand-mark--front {
    position: absolute;
    left: 420px;
    width: 310px;
    top: 80px;
    flex-direction: column;
    gap: 18px;
  }
  .brand-mark--front .brand-mark__circle { width: 130px; height: 130px; }
  .brand-mark--front .brand-mark__name { color: var(--ink); font-size: 30px; line-height: 1; white-space: nowrap; }

  .back-brand { position: absolute; left: 110px; top: 134px; }
  .back-brand .brand-mark { gap: 26px; }
  .back-brand .brand-mark__circle { width: 150px; height: 150px; }
  .back-brand__text { display: flex; flex-direction: column; gap: 14px; }
  .back-brand .brand-mark__name { color: var(--light-text); font-size: 42px; line-height: 1; white-space: nowrap; }
  .back-brand__phone { color: var(--light-text); font-size: 50px; font-weight: 700; line-height: 1; white-space: nowrap; }

  .product-line {
    position: absolute;
    left: 0; right: 0;
    top: 380px;
    margin: 0;
    text-align: center;
    color: var(--light-text);
    font-size: 18.5px;
    letter-spacing: 0.2px;
    white-space: nowrap;
  }
  .product-line__dot {
    display: inline-block;
    width: 7px; height: 7px;
    margin: 0 5px 2px;
    border-radius: 50%;
    background: var(--leaf-green);
  }
</style>
</head>
<body>
<main class="canvas">

  <section class="card card--front" aria-label="Card front">
    <svg class="front-swoosh" viewBox="0 0 800 456" aria-hidden="true">
      <path d="M0 290 C60 235 140 212 205 212 C325 212 425 292 470 384 C425 312 330 238 210 238 C140 238 60 262 0 316 Z" fill="var(--ink)"/>
      <path d="M0 320 C60 262 140 240 210 240 C330 240 440 320 496 456 L0 456 Z" fill="var(--brand-green)" stroke="var(--card-white)" stroke-width="4"/>
    </svg>
    <div class="brand-mark brand-mark--front">
      <span class="brand-mark__circle"></span>
      <span class="brand-mark__name">Birchwood Forage</span>
    </div>
    <div class="front-contact">
      <div class="front-contact__phone">847-302-1596</div>
      <div class="front-contact__social"><span class="social-dot"></span><span>@birchwoodforage</span></div>
    </div>
  </section>

  <section class="card card--back" aria-label="Card back">
    <div class="back-brand">
      <div class="brand-mark">
        <span class="brand-mark__circle"></span>
        <div class="back-brand__text">
          <span class="brand-mark__name">Birchwood Forage</span>
          <span class="back-brand__phone">847-302-1596</span>
        </div>
      </div>
    </div>
    <p class="product-line">Orchardgrass Hay<span class="product-line__dot"></span>Alfalfa Hay<span class="product-line__dot"></span>Mixed Grass Hay, &amp; Premium Quality Hay</p>
  </section>

</main>
</body>
</html>
```